Graphic to communicate emotional connection

Howdy-I need a graphic that describe my financial planning process.The attached is a concept, but please use your own creativity to show how you would display this:- The four circles on the outside (Protect what we have, know where it goes, make it grow, and dignity and independence) are the four major areas of concern- Then, there are three value statements:- The first is the most powerful which is that Clarity leads to Control which allows your Intentions to come through- The second shows that we take our clients from Uncertainty and Confusion, to Confidence and Intention- The third says we create space for you to develop your Purposeful Effort which leads to Your Best Financial Life.I've also attached my logo - please use the colors in my logo and maybe add a soft green as needed.The reader should be able to briefly scan this document and understand that we will connect with them on an emotional level to get their finances in shape.Thanks!-Ned

Target Market(s)

wealthy women, whether independent or married

Industry/Entity Type

Financial Planning

Requirements
Must have
• Please use the colors in my logo plus a soft green as needed
Should not have
• This should not be a busy or hard-to-read graphic. It is meant to convey an that I try to make an emotional connection, at a glance.

```html
<!DOCTYPE html>
<html lang="en">
<head>
<meta charset="utf-8">
<title>Harbor Lane Wealth Advisors – Our Planning Process</title>
<link href="https://fonts.googleapis.com/css2?family=Open+Sans:wght@700&display=swap" rel="stylesheet">
<style>
  :root {
    --navy: #243d7a;
    --slate: #676767;
    --overlap: #a8a8aa;
    --arrow: #a6a6a6;
    --rule-gray: #6a6a6a;
    --paper: #ffffff;
    --ink-light: #ffffff;
  }
  html, body {
    margin: 0;
    padding: 0;
    width: 1200px;
    height: 1200px;
    overflow: hidden;
    background: var(--paper);
  }
  .process-graphic {
    display: block;
    width: 1200px;
    height: 1200px;
    font-family: "Open Sans", Arial, sans-serif;
    font-weight: 700;
  }
  .circle-navy { fill: var(--navy); }
  .circle-slate { fill: var(--slate); }
  .circle-overlap { fill: var(--overlap); }
  .flow-arrow { fill: var(--arrow); }
  .rule-top { fill: var(--navy); }
  .rule-bottom { fill: var(--rule-gray); }
  .circle-label {
    fill: var(--ink-light);
    font-size: 20px;
    text-anchor: middle;
  }
  .circle-label-large {
    fill: var(--ink-light);
    font-size: 25px;
    text-anchor: middle;
  }
  .stage-label {
    fill: var(--navy);
    font-size: 25px;
    text-anchor: middle;
  }
  .core-statement {
    fill: var(--navy);
    font-size: 25px;
    text-anchor: middle;
  }
  .core-statement-sub {
    fill: var(--slate);
    font-size: 19px;
    text-anchor: middle;
  }
  .brand-mark { fill: var(--navy); }
  .brand-name {
    fill: var(--navy);
    font-size: 21px;
  }
</style>
</head>
<body>
<svg class="process-graphic" viewBox="0 0 1200 1200" xmlns="http://www.w3.org/2000/svg" role="img" aria-label="Financial planning process: clarity leads to control, allowing your intentions to come through; from uncertainty and confusion to confidence and intention; from purposeful effort to your best financial life">
  <defs>
    <clipPath id="clip-protect"><circle cx="153" cy="320" r="123"/></clipPath>
    <clipPath id="clip-know"><circle cx="1039" cy="286" r="124"/></clipPath>
    <clipPath id="clip-grow"><circle cx="152" cy="849" r="86"/></clipPath>
    <clipPath id="clip-leads"><circle cx="768" cy="751" r="113"/></clipPath>
  </defs>

  <!-- top rule -->
  <rect class="rule-top" x="29" y="101" width="1143" height="15"/>

  <!-- core value statement -->
  <g class="core-value">
    <text class="core-statement" x="592" y="238">CLARITY LEADS TO CONTROL</text>
    <text class="core-statement-sub" x="592" y="272">ALLOWING YOUR INTENTIONS TO COME THROUGH</text>
  </g>

  <!-- row one: protect / we take you from -->
  <g class="concern-pair">
    <circle class="circle-navy" cx="153" cy="320" r="123"/>
    <circle class="circle-slate" cx="279" cy="466" r="100"/>
    <circle class="circle-overlap" cx="279" cy="466" r="100" clip-path="url(#clip-protect)"/>
    <text class="circle-label" x="153" y="314">PROTECT WHAT</text>
    <text class="circle-label" x="153" y="341">WE HAVE</text>
    <text class="circle-label" x="279" y="472">WE TAKE</text>
    <text class="circle-label" x="279" y="499">YOU FROM</text>
  </g>

  <path class="flow-arrow" d="M342 461 H397 V449 L420 472 L397 495 V483 H342 Z"/>
  <text class="stage-label" x="511" y="461">UNCERTAINTY</text>
  <text class="stage-label" x="511" y="495">CONFUSION</text>

  <path class="flow-arrow" d="M608 459 H654 V447 L677 470 L654 493 V481 H608 Z"/>
  <text class="stage-label" x="773" y="458">CONFIDENCE</text>
  <text class="stage-label" x="773" y="492">INTENTION</text>

  <!-- know where it goes / to -->
  <g class="concern-pair">
    <circle class="circle-navy" cx="1039" cy="286" r="124"/>
    <circle class="circle-slate" cx="942" cy="392" r="69"/>
    <circle class="circle-overlap" cx="942" cy="392" r="69" clip-path="url(#clip-know)"/>
    <text class="circle-label" x="1034" y="274">KNOW WHERE</text>
    <text class="circle-label" x="1034" y="302">IT GOES</text>
    <text class="circle-label" x="930" y="411">TO</text>
  </g>

  <!-- row two: make it grow / we create space -->
  <g class="concern-pair">
    <circle class="circle-slate" cx="280" cy="766" r="112"/>
    <circle class="circle-navy" cx="152" cy="849" r="86"/>
    <circle class="circle-overlap" cx="280" cy="766" r="112" clip-path="url(#clip-grow)"/>
    <text class="circle-label" x="286" y="737">WE CREATE</text>
    <text class="circle-label" x="286" y="765">SPACE FOR YOUR</text>
    <text class="circle-label" x="130" y="832">MAKE</text>
    <text class="circle-label" x="130" y="860">IT</text>
    <text class="circle-label" x="130" y="888">GROW</text>
  </g>

  <path class="flow-arrow" d="M380 746 H438 V734 L461 757 L438 780 V768 H380 Z"/>
  <text class="stage-label" x="546" y="746">PURPOSEFUL</text>
  <text class="stage-label" x="546" y="781">EFFORT</text>

  <!-- which leads to / dignity & independence -->
  <g class="concern-pair">
    <circle class="circle-navy" cx="768" cy="751" r="113"/>
    <circle class="circle-slate" cx="886" cy="910" r="112"/>
    <circle class="circle-overlap" cx="886" cy="910" r="112" clip-path="url(#clip-leads)"/>
    <text class="circle-label" x="770" y="758">WHICH LEADS TO</text>
    <text class="circle-label-large" x="886" y="902">DIGNITY &amp;</text>
    <text class="circle-label-large" x="886" y="936">INDEPENDENCE</text>
  </g>

  <path class="flow-arrow" d="M889 731 H947 V719 L970 742 L947 765 V753 H889 Z"/>
  <text class="stage-label" x="1074" y="763">YOUR BEST</text>
  <text class="stage-label" x="1074" y="797">FINANCIAL LIFE</text>

  <!-- bottom rule and brand -->
  <rect class="rule-bottom" x="31" y="1084" width="810" height="16"/>
  <g class="brand">
    <rect class="brand-mark" x="862" y="1074" width="52" height="52"/>
    <text class="brand-name" x="926" y="1096">HARBOR LANE</text>
    <text class="brand-name" x="926" y="1122">WEALTH ADVISORS</text>
  </g>
</svg>
</body>
</html>
```